Quillstone Business Card

We need a business card design. We have a logo from a previous Sketchfold project and I am attaching the logo files in jpeg and photoshop.

```html
<!DOCTYPE html>
<html lang="en">
<head>
<meta charset="UTF-8">
<title>Quillstone Business Card</title>
<link href="https://fonts.googleapis.com/css2?family=Lato:wght@400;700;900&display=swap" rel="stylesheet">
<style>
  :root {
    --backdrop: #8f8f8f;
    --card: #222222;
    --ink: #ffffff;
    --ink-soft: #e4e4e4;
    --accent: #3fae49;
  }
  * { margin: 0; padding: 0; box-sizing: border-box; }
  html, body {
    width: 1200px;
    height: 900px;
    overflow: hidden;
  }
  body {
    background: var(--backdrop);
    display: flex;
    align-items: center;
    justify-content: center;
    font-family: "Lato", sans-serif;
  }
  .business-card {
    position: relative;
    width: 1000px;
    height: 572px;
    background: var(--card);
    color: var(--ink);
    padding: 100px 0 0 84px;
  }
  .brand {
    display: flex;
    align-items: center;
    gap: 18px;
  }
  .brand-mark {
    width: 52px;
    height: 52px;
    background: var(--accent);
  }
  .brand-name {
    font-weight: 900;
    font-size: 60px;
    letter-spacing: -0.5px;
    color: var(--ink);
    line-height: 1;
  }
  .holder {
    margin-top: 74px;
  }
  .holder-name {
    font-size: 42px;
    font-weight: 400;
    line-height: 1.1;
  }
  .holder-name strong { font-weight: 700; }
  .holder-title {
    margin-top: 8px;
    font-size: 22px;
    color: var(--ink-soft);
  }
  .contact-list {
    list-style: none;
    margin-top: 70px;
  }
  .contact-item {
    display: flex;
    align-items: center;
    gap: 14px;
    font-size: 27px;
    line-height: 1;
    letter-spacing: 0.6px;
    margin-bottom: 12px;
  }
  .contact-icon {
    width: 22px;
    height: 22px;
    flex: none;
    fill: var(--accent);
  }
</style>
</head>
<body>
  <article class="business-card">
    <header class="brand">
      <span class="brand-mark"></span>
      <span class="brand-name">Quillstone</span>
    </header>

    <section class="holder">
      <h1 class="holder-name">John <strong>Smith</strong></h1>
      <p class="holder-title">Title goes here</p>
    </section>

    <ul class="contact-list">
      <li class="contact-item">
        <svg class="contact-icon" viewBox="0 0 24 24" aria-hidden="true">
          <path d="M3 9c0-3 4-5 9-5s9 2 9 5v2h-5V8.5c-1-.6-2.5-.9-4-.9s-3 .3-4 .9V11H3z"/>
          <rect x="5" y="12" width="14" height="9" rx="1.5"/>
        </svg>
        <span>123-456-7890</span>
      </li>
      <li class="contact-item">
        <svg class="contact-icon" viewBox="0 0 24 24" aria-hidden="true">
          <path d="M2 5h20v2l-10 6L2 7z"/>
          <path d="M2 9l10 6 10-6v10H2z"/>
        </svg>
        <span>yourdomain.com</span>
      </li>
      <li class="contact-item">
        <svg class="contact-icon" viewBox="0 0 24 24" aria-hidden="true">
          <path d="M10.6 13.4a1 1 0 0 1 0-1.4l4-4a1 1 0 1 1 1.4 1.4l-4 4a1 1 0 0 1-1.4 0z"/>
          <path d="M13 6l2-2a4.2 4.2 0 0 1 6 6l-2 2-1.5-1.5 2-2a2.1 2.1 0 0 0-3-3l-2 2z"/>
          <path d="M11 18l-2 2a4.2 4.2 0 0 1-6-6l2-2 1.5 1.5-2 2a2.1 2.1 0 0 0 3 3l2-2z"/>
        </svg>
        <span>yourname@yourdomain.com</span>
      </li>
      <li class="contact-item">
        <svg class="contact-icon" viewBox="0 0 24 24" aria-hidden="true">
          <path d="M12 3l10 9h-3v9h-5v-6h-4v6H5v-9H2z"/>
        </svg>
        <span>Street address goes here, Suite #303, Alt Bldg, NY 82365</span>
      </li>
    </ul>
  </article>
</body>
</html>
```